Private Optometric Practice Needs new Presentation Folders/Stationary

We recently moved our office and are looking to refresh our presentation folders and stationary. I tend to prefer simple, clean designs. We are a full scope optometric practice provide high quality eyewear, custom contact lenses, along with emergency care and treatment for dry eyes. We communicate with a lot of other doctors and want to exude professionalism. I have attached 2 versions of our logo.

Target Market(s)

Familys

Industry/Entity Type

Eyecare

Font styles to use
Sans Serif

Colors
0054AA
0677BA
7BADD7
CADEEF
E8F1F8

Requirements
Nice to have
• Bifold, areas to put information about practice, welcome letter

```html
<!DOCTYPE html>
<html lang="en">
<head>
<meta charset="utf-8">
<title>Clearview Vision – Business Card</title>
<link rel="stylesheet" href="https://fonts.googleapis.com/css2?family=Montserrat:wght@300;400;500;600&display=swap">
<style>
  :root {
    --page-bg: #e0e0e0;
    --card-navy: #061822;
    --brand-blue: #38a9e0;
    --text-light: #ffffff;
    --font-main: "Montserrat", Arial, sans-serif;
  }
  * { box-sizing: border-box; margin: 0; padding: 0; }
  html, body {
    width: 1200px;
    height: 1200px;
    overflow: hidden;
    background: var(--page-bg);
    font-family: var(--font-main);
  }
  .business-card {
    position: absolute;
    left: 79px;
    top: 295px;
    width: 1042px;
    height: 610px;
    background: var(--card-navy);
    overflow: hidden;
  }
  .brand-panel {
    position: absolute;
    left: 0;
    top: 0;
    width: 496px;
    height: 100%;
    background: var(--brand-blue);
    display: flex;
    align-items: center;
    justify-content: center;
  }
  .brand-name {
    color: var(--card-navy);
    font-weight: 500;
    font-size: 34px;
    letter-spacing: 6px;
    text-transform: uppercase;
    text-align: center;
    line-height: 1.3;
  }
  .contact-panel {
    position: absolute;
    left: 544px;
    top: 0;
    right: 0;
    height: 100%;
    color: var(--text-light);
  }
  .doctor-name {
    position: absolute;
    top: 152px;
    left: 0;
    font-weight: 600;
    font-size: 27px;
    letter-spacing: 1px;
    text-transform: uppercase;
    white-space: nowrap;
  }
  .contact-row {
    position: absolute;
    left: 0;
    display: flex;
    align-items: flex-start;
    font-weight: 400;
    font-size: 21px;
    letter-spacing: 0.5px;
    text-transform: uppercase;
    line-height: 29px;
    white-space: nowrap;
  }
  .contact-row .icon {
    width: 18px;
    height: 18px;
    margin-top: 5px;
    margin-right: 19px;
    flex: none;
  }
  .row-address { top: 244px; }
  .row-phone { top: 393px; }
  .row-web { top: 425px; }
  .icon path, .icon circle, .icon ellipse, .icon line {
    fill: none;
    stroke: var(--text-light);
    stroke-width: 1.8;
    stroke-linecap: round;
    stroke-linejoin: round;
  }
  .icon .solid { fill: var(--text-light); stroke: none; }
</style>
</head>
<body>
  <div class="business-card">
    <div class="brand-panel">
      <p class="brand-name">Clearview<br>Vision</p>
    </div>

    <div class="contact-panel">
      <h1 class="doctor-name">Daniel Whitford, O.D.</h1>

      <div class="contact-row row-address">
        <svg class="icon" viewBox="0 0 18 18" aria-hidden="true">
          <path d="M9 16 C5 11 4 9 4 7 A5 5 0 0 1 14 7 C14 9 13 11 9 16 Z"/>
          <circle cx="9" cy="7" r="1.8"/>
          <path d="M4 16 H14"/>
        </svg>
        <address style="font-style: normal;">4120 Lakeview Pkwy.<br>Suite B<br>Millbrook, MI 48010</address>
      </div>

      <div class="contact-row row-phone">
        <svg class="icon" viewBox="0 0 18 18" aria-hidden="true">
          <path class="solid" d="M4.5 1.5 L7 1.5 L8 5.5 L6.3 7 C7.2 9 9 10.8 11 11.7 L12.5 10 L16.5 11 L16.5 13.5 C16.5 15 15 16.5 13.5 16.3 C7.5 15.6 2.4 10.5 1.7 4.5 C1.5 3 3 1.5 4.5 1.5 Z"/>
        </svg>
        <span>555-014-2287</span>
      </div>

      <div class="contact-row row-web">
        <svg class="icon" viewBox="0 0 18 18" aria-hidden="true">
          <circle cx="9" cy="9" r="7.5"/>
          <ellipse cx="9" cy="9" rx="3.2" ry="7.5"/>
          <line x1="1.5" y1="9" x2="16.5" y2="9"/>
          <path d="M2.8 5 H15.2 M2.8 13 H15.2"/>
        </svg>
        <span>www.myclearviewvision.com</span>
      </div>
    </div>
  </div>
</body>
</html>
```